Brightvantage.com tech company website

Current site is www.brightvantage.com. The site will tell you about our company.

Designs we like are:
http://megainfo.quellorix.com
www.trelvo.com
www.morvasket.com

Target Market(s)

B2B

Industry/Entity Type

It Company

Coding

Coded - Design and coding required

Number of Pages Required

5+ page

Requirements
Must have
• We want to entice without giving away too much info. We like graphics and colors. But website must look official and credible.

```html
<!DOCTYPE html>
<html lang="en">
<head>
<meta charset="utf-8">
<title>Bright Vantage</title>
<link href="https://fonts.googleapis.com/css2?family=Oswald:wght@400;500&family=Roboto:wght@300;400;700&display=swap" rel="stylesheet">
<style>
:root{
  --brand:#1d5b8d;
  --brand-light:#2c7cb8;
  --ink:#3a3a3a;
  --muted:#7a7a7a;
  --pale:#ececec;
  --white:#ffffff;
  --footer:#262626;
  --sky-top:#c9d3dc;
  --sky-mid:#7d8ea0;
  --sky-low:#2e3f52;
}
*{box-sizing:border-box;margin:0;padding:0}
html,body{width:1200px;height:3100px;overflow:hidden}
body{font-family:'Roboto',sans-serif;color:var(--ink);background:var(--white);position:relative}
.btn{display:inline-block;background:var(--brand);color:var(--white);font:400 20px 'Roboto',sans-serif;padding:14px 28px;border-radius:4px;text-transform:uppercase;letter-spacing:.5px}
section{position:relative;width:1200px}

/* hero */
.hero{height:650px;overflow:hidden}
.hero-photo{position:absolute;inset:0;background:linear-gradient(180deg,var(--sky-top) 0%,#aebccb 35%,var(--sky-mid) 65%,var(--sky-low) 100%)}
.nav{position:absolute;top:28px;left:0;width:100%;display:flex;justify-content:center;gap:14px}
.nav a{font:400 19px 'Roboto',sans-serif;color:var(--white);padding:16px 26px;text-transform:uppercase;text-decoration:none}
.nav a.active{background:var(--brand);border-radius:4px}
.nav-bar{position:absolute;top:28px;left:200px;width:800px;height:56px;background:rgba(255,255,255,.12)}
.logo{position:absolute;top:170px;width:100%;display:flex;justify-content:center;align-items:center;gap:22px}
.logo-mark{width:60px;height:60px;background:var(--brand)}
.logo-name{font:700 84px 'Roboto',sans-serif;color:var(--brand);text-transform:uppercase;letter-spacing:1px}
.tagline{position:absolute;top:430px;width:100%;text-align:center;font:400 52px 'Oswald',sans-serif;color:var(--white);letter-spacing:2px;text-transform:uppercase}
.notch{position:absolute;left:0;bottom:0;width:100%;height:40px}

/* welcome */
.welcome{height:410px;background:var(--pale);text-align:center;padding-top:50px}
.welcome h1{font:300 54px 'Roboto',sans-serif;color:var(--ink)}
.welcome h1 span{color:var(--brand-light)}
.welcome p{width:900px;margin:26px auto 0;font-size:17px;line-height:1.6;color:var(--muted)}
.welcome .btn{margin-top:32px}

/* features */
.feature{display:flex;align-items:center}
.bigdata{height:390px;background:var(--white)}
.perception{height:470px;background:var(--pale)}
.art{border-radius:4px;flex:none}
.bigdata .art{width:440px;height:300px;margin-left:110px;background:radial-gradient(circle at 50% 55%,#5d8fc4 0%,#9dbde0 40%,#ffffff 75%)}
.bigdata .copy{margin-left:100px;width:480px}
.perception .copy{margin-left:70px;width:520px}
.perception .art{width:500px;height:330px;margin-left:30px;background:linear-gradient(135deg,#1c2e45 0%,#3b5e86 50%,#182435 100%)}
.copy h2{font:300 46px 'Roboto',sans-serif;color:var(--brand-light);white-space:nowrap}
.copy p{margin:20px 0 28px;font-size:17px;line-height:1.6;color:var(--muted);max-width:450px}

/* banner */
.banner{height:260px;background:linear-gradient(90deg,#0f3a63 0%,#1d5b8d 50%,#113e66 100%);text-align:center;padding:66px 100px 0}
.banner h2{font:500 40px 'Oswald',sans-serif;color:var(--white);text-transform:uppercase;letter-spacing:1px;white-space:nowrap}
.banner .callback{display:inline-block;margin-top:26px;background:var(--white);color:#111;font:700 22px 'Roboto',sans-serif;padding:14px 24px;border-radius:4px}

/* news */
.news{height:340px;background:var(--white);padding-top:40px}
.news h2{text-align:center;font:400 54px 'Roboto',sans-serif;color:var(--ink)}
.news h2 span{color:var(--brand-light)}
.news-list{display:flex;justify-content:center;gap:60px;margin-top:36px}
.news-item{display:flex;gap:18px;width:300px}
.date{width:80px;flex:none;text-align:center;border-radius:3px;overflow:hidden;align-self:flex-start}
.date .day{background:var(--brand);color:var(--white);font:400 40px 'Roboto',sans-serif;padding:8px 0}
.date .month{background:#4a4a4a;color:var(--white);font-size:20px;padding:4px 0}
.news-item h3{font:700 16px 'Roboto',sans-serif;color:var(--brand);line-height:1.3}
.news-item p{font-size:13px;color:var(--muted);line-height:1.4;margin:8px 0}
.news-item a{font:700 13px 'Roboto',sans-serif;color:var(--ink);text-decoration:underline}

/* contact */
.contact{height:470px;background:linear-gradient(180deg,#ffffff 0%,#f1f3f5 45%,#b9c3cd 100%);border-top:6px solid var(--brand);padding-top:30px}
.contact h2{text-align:center;font:300 54px 'Roboto',sans-serif;color:var(--brand-light)}
.contact-body{display:flex;margin-top:34px}
.form{margin-left:80px;width:420px}
.field{width:420px;height:46px;border:1px solid #9aa6b2;background:var(--white);font-size:15px;color:#666;padding:12px;margin-bottom:16px}
.field.msg{height:96px}
.form .btn{padding:12px 36px}
.info{margin-left:240px;width:360px}
.info-row{display:flex;gap:16px;margin-bottom:18px;font-size:16px;color:#555;line-height:1.45}
.info-row svg{flex:none}
.info-row strong{display:block;color:var(--brand);font-weight:400;font-size:18px}
.social{display:flex;gap:12px;margin-top:10px}
.social span{width:52px;height:52px;background:var(--brand);border-radius:3px;display:flex;align-items:center;justify-content:center}
.up-tab{position:absolute;bottom:0;left:0;width:100%;height:40px}

/* footer */
.footer{height:130px;background:var(--footer);text-align:center;padding-top:30px}
.footer nav{display:flex;justify-content:center;gap:44px}
.footer nav a{color:var(--white);font-size:16px;text-decoration:none}
.footer p{color:#bbb;font-size:14px;margin-top:24px}
.footer p b{color:var(--white);text-decoration:underline}
</style>
</head>
<body>

<section class="hero">
  <div class="hero-photo" role="img" aria-label="City skyline at dawn with tall towers under a hazy sky"></div>
  <div class="nav-bar"></div>
  <nav class="nav">
    <a class="active">Home</a><a>About</a><a>Services</a><a>Case Studies</a><a>Contact</a>
  </nav>
  <div class="logo"><span class="logo-mark"></span><span class="logo-name">Bright Vantage</span></div>
  <div class="tagline">Existing Capabilities, Systems &amp; Services</div>
  <svg class="notch" viewBox="0 0 1200 40" width="1200" height="40">
    <path d="M0 40 H540 L560 8 H640 L660 40 H1200 Z" fill="#ececec"/>
    <path d="M588 20 L600 30 L612 20" stroke="#555" stroke-width="3" fill="none"/>
  </svg>
</section>

<section class="welcome">
  <h1>Welcome to <span>Bright Vantage</span></h1>
  <p>Bright Vantage was created to sell, to the commercial sector, existing capabilities, systems, and services, developed over the last decade for the US government security apparatus.</p>
  <p>Specific assignments involving Big Data gathering, enhancement, and analytics, as well as perception and influence activities, have proven to be highly relevant and easily transferable for business uses.</p>
  <span class="btn">Read More</span>
</section>

<section class="feature bigdata">
  <div class="art" role="img" aria-label="Tablet showing rising bar chart and pie chart graphics"></div>
  <div class="copy">
    <h2>Big Data and Analytics</h2>
    <p>Bright Vantage is expert at data collection and analysis, extracting the data important to business, and putting it into a format most useful to the C suite.</p>
    <span class="btn">Read More</span>
  </div>
</section>

<section class="feature perception">
  <div class="copy">
    <h2>Perception and Influence</h2>
    <p>Your reputation is important. An integrated, holistic and strategic approach is necessary to maintain positive corporate recognition, brand loyalty and consumer confidence.</p>
    <span class="btn">Read More</span>
  </div>
  <div class="art" role="img" aria-label="Business professionals working with glowing digital interface screens"></div>
</section>

<section class="banner" role="img" aria-label="Dark blue network background">
  <h2>Bright Vantage is expert at data collection and analysis</h2>
  <span class="callback">Request a Call Back</span>
</section>

<section class="news">
  <h2>Latest <span>News</span></h2>
  <div class="news-list">
    <div class="news-item">
      <div class="date"><div class="day">11</div><div class="month">Sep</div></div>
      <div><h3>Lorem Ipsum is simply dummy text of the print</h3><p>Lorem Ipsum is simply dummy text of the printing and typesetting industry...</p><a>READ MORE</a></div>
    </div>
    <div class="news-item">
      <div class="date"><div class="day">10</div><div class="month">Sep</div></div>
      <div><h3>Lorem Ipsum is simply dummy text of the print</h3><p>Lorem Ipsum is simply dummy text of the printing and typesetting industry...</p><a>READ MORE</a></div>
    </div>
    <div class="news-item">
      <div class="date"><div class="day">09</div><div class="month">Sep</div></div>
      <div><h3>Lorem Ipsum is simply dummy text of the print</h3><p>Lorem Ipsum is simply dummy text of the printing and typesetting industry...</p><a>READ MORE</a></div>
    </div>
  </div>
</section>

<section class="contact">
  <h2>Contact Us</h2>
  <div class="contact-body">
    <div class="form">
      <div class="field">Enter Name</div>
      <div class="field">Enter E-Mail</div>
      <div class="field msg">Message</div>
      <span class="btn">Send</span>
    </div>
    <div class="info">
      <div class="info-row">
        <svg width="22" height="28" viewBox="0 0 22 28"><path d="M11 1a9 9 0 0 0-9 9c0 7 9 17 9 17s9-10 9-17a9 9 0 0 0-9-9z" fill="#1d5b8d"/><circle cx="11" cy="10" r="3.5" fill="#fff"/></svg>
        <div><strong>Bright Vantage</strong>Lorem ipsum is simply dummy text of the printing</div>
      </div>
      <div class="info-row">
        <svg width="22" height="22" viewBox="0 0 24 24"><path d="M6.6 10.8a15 15 0 0 0 6.6 6.6l2.2-2.2a1 1 0 0 1 1-.25 11.4 11.4 0 0 0 3.6.6 1 1 0 0 1 1 1V20a1 1 0 0 1-1 1A17 17 0 0 1 3 4a1 1 0 0 1 1-1h3.5a1 1 0 0 1 1 1c0 1.25.2 2.45.6 3.6a1 1 0 0 1-.25 1z" fill="#555"/></svg>
        <div>555-201-4730</div>
      </div>
      <div class="info-row">
        <svg width="22" height="18" viewBox="0 0 24 18"><rect x="1" y="1" width="22" height="16" rx="2" fill="#555"/><path d="M2 3l10 7 10-7" stroke="#fff" stroke-width="2" fill="none"/></svg>
        <div>info@brightvantage.com</div>
      </div>
      <div class="social">
        <span aria-label="Share"><svg width="24" height="24" viewBox="0 0 24 24"><circle cx="18" cy="5" r="3" fill="#fff"/><circle cx="6" cy="12" r="3" fill="#fff"/><circle cx="18" cy="19" r="3" fill="#fff"/><path d="M6 12L18 5M6 12l12 7" stroke="#fff" stroke-width="2"/></svg></span>
        <span aria-label="Chat"><svg width="24" height="24" viewBox="0 0 24 24"><path d="M3 4h18v12H9l-5 4v-4H3z" fill="#fff"/></svg></span>
        <span aria-label="Website"><svg width="24" height="24" viewBox="0 0 24 24"><circle cx="12" cy="12" r="9" fill="none" stroke="#fff" stroke-width="2"/><path d="M3 12h18M12 3c3 3 3 15 0 18M12 3c-3 3-3 15 0 18" stroke="#fff" stroke-width="1.6" fill="none"/></svg></span>
        <span aria-label="Email"><svg width="24" height="20" viewBox="0 0 24 18"><rect x="1" y="1" width="22" height="16" rx="2" fill="#fff"/><path d="M2 3l10 7 10-7" stroke="#1d5b8d" stroke-width="2" fill="none"/></svg></span>
      </div>
    </div>
  </div>
  <svg class="up-tab" viewBox="0 0 1200 40" width="1200" height="40">
    <path d="M0 40 H540 L560 8 H640 L660 40 H1200 Z" fill="#262626"/>
    <path d="M588 28 L600 18 L612 28" stroke="#fff" stroke-width="3" fill="none"/>
  </svg>
</section>

<footer class="footer">
  <nav><a>Home</a><a>About</a><a>Services</a><a>Case Studies</a><a>Contact</a></nav>
  <p>© <b>Bright Vantage</b> 2015, All Rights Reserved.</p>
</footer>

</body>
</html>
```